Web Design for UK Based Technology Company*

Korvane is a new entrant in the data marketplace.
It is offering two direct API services to help clients access:
- Company Data
- Location Data
We also offer data services and consulting to help companies to integrate our API services and the data derived from them into their businesses. Our aim is to offer both the technology and services to help businesses use and integrate data better. It is a modern business built to support a modern world.

Target Market(s)

Business Professionals and decision makers

Industry/Entity Type

It Service

Number of Pages Required

5+ page

Font styles to use
Sans Serif

Colors

Designer to choose colors to be used in the design.

Requirements
Must have
• The full suite of PSD designs taking into account the layouts and wireframes supplied with which it will be compared. Focus on the homepage first. It has to have a consistent theme/feel. It has to fit with the logo.
Nice to have
• Simple, clean, a few strong ideas.
Should not have
• Cartoons, overdesign, loud colours.

```html
<!DOCTYPE html>
<html lang="en">
<head>
<meta charset="utf-8">
<title>Korvane – Richer Data to Drive Your Business</title>
<link rel="stylesheet" href="https://fonts.googleapis.com/css2?family=Montserrat:wght@400;500;600;700&display=swap">
<style>
:root{
  --brand:#1a6fb5;
  --brand-dark:#135a95;
  --brand-light:#2a93dc;
  --ink:#1d1d1f;
  --body:#6d6f73;
  --muted:#9a9ca0;
  --soft:#f6f7f9;
  --white:#ffffff;
  --night:#1e1f21;
  --accent:#f57b2a;
  --accent-2:#ffb13a;
}
*{box-sizing:border-box;margin:0;padding:0}
html,body{width:1200px;height:3482px;overflow:hidden;background:var(--white)}
body{font-family:"Montserrat",Arial,sans-serif;color:var(--ink)}
.page{position:relative;width:1200px;height:3482px;overflow:hidden}
section,header,footer{position:absolute;left:0;width:1200px}
.abs{position:absolute}
.btn{position:absolute;display:flex;align-items:center;justify-content:center;height:30px;border-radius:15px;font-size:10px;font-weight:700;letter-spacing:1px;text-transform:uppercase}
.btn-outline{border:2px solid var(--brand);color:var(--brand);background:var(--white)}
.btn-solid{background:var(--brand);color:var(--white)}
.btn-ghost{border:2px solid var(--white);color:var(--white)}
.btn-white{background:var(--white);color:var(--brand)}
.center{text-align:center;left:0;width:1200px}

/* header */
.site-header{top:0;height:97px;background:var(--white);box-shadow:0 2px 6px rgba(0,0,0,.06);z-index:2}
.brand-name{left:88px;top:26px;font-size:34px;font-weight:700;color:var(--ink);letter-spacing:1px;display:flex;align-items:center;gap:12px}
.brand-name .dot{width:26px;height:26px;border-radius:50%;background:var(--brand)}
.call{left:678px;top:23px;font-size:14px;color:var(--brand);font-weight:500}
.call b{font-weight:700}
.nav{left:430px;top:65px;display:flex;gap:0;font-size:10px;font-weight:700;letter-spacing:.6px;text-transform:uppercase}
.nav span{position:absolute;white-space:nowrap;color:var(--ink)}
.nav .active{color:var(--brand-light)}

/* hero */
.hero{top:97px;height:543px;background:linear-gradient(120deg,#3d3b3a,#6b5f55 45%,#4b4e55 80%,#2e3238)}
.hero::after{content:"";position:absolute;inset:0;background:rgba(20,22,28,.45)}
.hero *{z-index:1}
.hero h1{position:absolute;top:105px;font-size:37px;font-weight:500;color:var(--white)}
.hero-divider{left:600px;top:200px;width:1px;height:248px;background:rgba(255,255,255,.45)}
.hero-col{width:600px;text-align:center;color:var(--white)}
.hero-col h2{font-size:23px;font-weight:600;line-height:30px;margin-top:28px}
.hero-col svg{display:block;margin:0 auto}

/* about */
.about{top:640px;height:416px;background:var(--soft)}
.about .mark{top:80px;font-size:34px;font-weight:700;color:var(--brand)}
.about h2{top:170px;font-size:24px;font-weight:600;color:var(--brand)}
.about p{left:220px;width:760px;top:212px;font-size:13px;line-height:21px;color:var(--body);text-align:center}

/* products */
.products{top:1056px;height:824px;background:var(--white)}
.screen{position:absolute;border-radius:10px;background:var(--white);box-shadow:0 8px 28px rgba(0,0,0,.12);padding:12px}
.screen .fill{width:100%;height:100%;border-radius:4px}
.laptop-base{position:absolute;height:10px;border-radius:0 0 60px 60px;background:linear-gradient(#e6e8ec,#c9ccd2)}
.badge{position:absolute;border-radius:50%;background:radial-gradient(circle at 40% 35%,var(--accent-2),var(--accent));color:var(--white);display:flex;flex-direction:column;align-items:center;justify-content:center;text-align:center;box-shadow:0 4px 10px rgba(245,123,42,.35)}
.badge small{font-size:11px;font-weight:600}
.badge strong{font-size:17px;font-weight:700}
.eyebrow{font-size:13px;font-weight:700;letter-spacing:1px;color:var(--brand);text-transform:uppercase}
.product-title{font-size:23px;font-weight:500;line-height:31px;color:var(--ink)}

/* cta */
.cta{top:1880px;height:367px;background:linear-gradient(120deg,#1c7cc6 0%,#2b8fd6 35%,#1a6fb5 70%,#2784cc 100%);color:var(--white)}
.cta .mark{top:70px;font-size:30px;font-weight:700}
.cta h2{top:140px;font-size:24px;font-weight:600}
.cta p{left:220px;width:760px;top:176px;font-size:13px;line-height:21px;text-align:center;color:rgba(255,255,255,.9)}

/* demand */
.demand{top:2247px;height:522px;background:var(--white)}
.photo{position:absolute;box-shadow:0 10px 24px rgba(0,0,0,.18)}
.demand h2{left:513px;top:88px;font-size:25px;font-weight:600;line-height:30px}
.demand p{position:absolute;left:513px;width:600px;font-size:13px;line-height:24px;color:var(--body)}
.ticks{position:absolute;left:513px;top:233px;list-style:none;font-size:13px;line-height:24.5px;color:var(--body)}
.ticks li{display:flex;align-items:center;gap:10px}
.demand .phone{color:var(--brand);font-weight:700}

/* where */
.where{top:2769px;height:364px}
.where-info{position:absolute;left:0;top:0;width:600px;height:364px;background:var(--night);color:var(--white)}
.where-info .eyebrow{position:absolute;left:88px;top:90px;color:var(--brand-light)}
.address{position:absolute;left:88px;top:130px;font-size:13px;line-height:21px;color:#d6d7da;width:440px}
.where-call{position:absolute;left:88px;top:184px;font-size:20px;font-weight:600;color:var(--brand-light)}
.map{position:absolute;left:600px;top:0;width:600px;height:364px;background:linear-gradient(135deg,#e9ebe6,#eef0ec 50%,#dfe9d9)}

/* footer */
.site-footer{top:3133px;height:349px;background:linear-gradient(120deg,#2a97df,#1e86d2 50%,#2b9be2);color:var(--white)}
.fcol{position:absolute;top:84px}
.fcol h3{font-size:13px;font-weight:700;letter-spacing:.8px;text-transform:uppercase;margin-bottom:14px}
.fcol li{list-style:none;font-size:13px;line-height:24px;color:rgba(255,255,255,.92)}
.footer-mark{left:1060px;top:76px;font-size:20px;font-weight:700}
.footer-rule{left:88px;top:272px;width:1024px;height:1px;background:rgba(255,255,255,.35)}
.copy{left:88px;top:303px;font-size:12px}
.legal{right:88px;top:303px;font-size:12px;display:flex;gap:14px}
</style>
</head>
<body>
<div class="page">

<header class="site-header">
  <div class="abs brand-name"><span class="dot"></span>KORVANE</div>
  <div class="abs call">Call Us: <b>123-456-7890</b></div>
  <div class="btn btn-solid" style="left:877px;top:16px;width:114px;height:32px">
    <svg width="12" height="12" viewBox="0 0 12 12" style="margin-right:6px"><circle cx="6" cy="4" r="2.6" fill="#fff"/><path d="M1 12c0-3 2.3-4.6 5-4.6S11 9 11 12z" fill="#fff"/></svg>Login</div>
  <div class="btn btn-solid" style="left:1000px;top:16px;width:110px;height:32px;background:var(--brand-dark)">Free Trial</div>
  <nav class="abs nav">
    <span class="active" style="left:0">Home</span>
    <span style="left:74px">Company Data</span>
    <span style="left:213px">Company Information</span>
    <span style="left:410px">Services</span>
    <span style="left:508px">Pricing</span>
    <span style="left:603px">Contact Us</span>
  </nav>
</header>

<section class="hero" role="img" aria-label="Photo of a team working together at a desk with laptops">
  <h1 class="center">Richer Data to Drive Your Business</h1>
  <div class="abs hero-divider"></div>
  <div class="abs hero-col" style="left:0;top:215px">
    <svg width="54" height="44" viewBox="0 0 54 44"><rect x="3" y="10" width="48" height="32" rx="4" fill="#2a93dc"/><rect x="18" y="3" width="18" height="9" rx="2" fill="none" stroke="#2a93dc" stroke-width="3"/><rect x="3" y="20" width="48" height="3" fill="#1a6fb5"/><rect x="23" y="18" width="8" height="8" rx="1" fill="#fff"/></svg>
    <h2>Comprehensive Company<br>Information</h2>
    <div class="btn btn-ghost" style="left:228px;top:138px;width:144px;height:28px">Company API</div>
  </div>
  <div class="abs hero-col" style="left:600px;top:210px">
    <svg width="50" height="50" viewBox="0 0 50 50"><path d="M25 3a12 12 0 0 1 12 12c0 9-12 22-12 22S13 24 13 15A12 12 0 0 1 25 3z" fill="#2a93dc"/><circle cx="25" cy="15" r="4.5" fill="#fff"/><path d="M6 47l7-14h7M44 47l-7-14h-7M6 47h38" fill="none" stroke="#2a93dc" stroke-width="3" stroke-linejoin="round"/></svg>
    <h2>Bring Mapping Data Into<br>Your Business</h2>
    <div class="btn btn-solid" style="left:228px;top:143px;width:144px;height:28px;background:var(--brand-light)">Location API</div>
  </div>
</section>

<section class="about">
  <div class="abs center mark">KORVANE</div>
  <h2 class="abs center">Korvane is setup for connected world.</h2>
  <p class="abs">A world where data is integrated, comprehensive and useful. There are many variations of passages of Lorem Ipsum available, but the majority have suffered alteration in some form, by injected humour, or randomised words which don't look even slightly believable.</p>
  <div class="btn btn-outline" style="left:529px;top:302px;width:174px">About Us</div>
</section>

<section class="products">
  <div class="screen" style="left:110px;top:77px;width:453px;height:285px">
    <div class="fill" role="img" aria-label="Company data dashboard screenshot with charts" style="background:linear-gradient(120deg,#f4f5f8 0%,#f7e3f1 30%,#f3f0fb 55%,#eef0f6 100%)"></div>
  </div>
  <div class="laptop-base" style="left:88px;top:362px;width:497px"></div>
  <div class="badge" style="left:464px;top:58px;width:104px;height:104px"><small>From Only</small><strong>£29pm</strong></div>
  <div class="abs eyebrow" style="left:615px;top:128px">Company API</div>
  <div class="abs product-title" style="left:615px;top:164px;width:520px">Your supply one or more company numbers - we send back everything via a simple API or CSV file</div>
  <div class="btn btn-outline" style="left:615px;top:286px;width:146px">Find Out More</div>
  <div class="btn btn-solid" style="left:770px;top:286px;width:112px">Free Trial</div>

  <div class="abs eyebrow" style="left:88px;top:475px">Location API</div>
  <div class="abs product-title" style="left:88px;top:512px;width:470px">You send us a postcode we send you the location. or you send us the location, we send back the postcode: API or CSV.</div>
  <div class="btn btn-outline" style="left:88px;top:664px;width:140px">Find Out More</div>
  <div class="btn btn-solid" style="left:239px;top:664px;width:114px">Free Trial</div>
  <div class="screen" style="left:637px;top:441px;width:451px;height:290px">
    <div class="fill" role="img" aria-label="Map of the Mediterranean region with plotted location markers" style="background:linear-gradient(135deg,#c9d9ea 0%,#d8d3c4 40%,#c6d4e6 70%,#d9cfc0 100%)"></div>
  </div>
  <div class="laptop-base" style="left:615px;top:731px;width:495px"></div>
  <div class="badge" style="left:645px;top:420px;width:93px;height:93px"><small>From Only</small><strong>£29pm</strong></div>
</section>

<section class="cta">
  <div class="abs center mark">KORVANE</div>
  <h2 class="abs center">Go ahead: test our data; or let's talk it through ...</h2>
  <p class="abs">Lorem Ipsum is simply dummy text of the printing and typesettin industry. There are many variations of passages of Lorem Ipsum available, but the majority have suffered alteration in some form, by injected humour, or randomised words which standard dummy text.</p>
  <div class="btn btn-ghost" style="left:436px;top:267px;width:158px">Call: 123-456-7890</div>
  <div class="btn btn-white" style="left:603px;top:267px;width:158px">Send an Email</div>
</section>

<section class="demand">
  <div class="photo" role="img" aria-label="Photo of two colleagues reviewing documents at a desk" style="left:88px;top:86px;width:360px;height:359px;background:linear-gradient(135deg,#6f8aa3,#b7c2c9 45%,#8a7a6c 75%,#4e5a68)"></div>
  <h2 class="abs">Demand data requirments?<br>look no further</h2>
  <p style="top:160px">Lorem Ipsum is simply dummy text of the printing and typesetting industry. Lorem Ipsum has been the industry's standard dummy text ever since the 1500s, when an unknown printer took a galley.</p>
  <ul class="ticks">
    <li><svg width="13" height="13" viewBox="0 0 13 13"><circle cx="6.5" cy="6.5" r="6.5" fill="#2a93dc"/><path d="M3.5 6.7l2 2 4-4.2" fill="none" stroke="#fff" stroke-width="1.6"/></svg>Contrary to popular belief, Lorem Ipsum is not simply random</li>
    <li><svg width="13" height="13" viewBox="0 0 13 13"><circle cx="6.5" cy="6.5" r="6.5" fill="#2a93dc"/><path d="M3.5 6.7l2 2 4-4.2" fill="none" stroke="#fff" stroke-width="1.6"/></svg>There are many variations of passages of Lorem Ipsum available, majority</li>
    <li><svg width="13" height="13" viewBox="0 0 13 13"><circle cx="6.5" cy="6.5" r="6.5" fill="#2a93dc"/><path d="M3.5 6.7l2 2 4-4.2" fill="none" stroke="#fff" stroke-width="1.6"/></svg>Lorem Ipsum is simply dummy text of the printing and typesetting industry</li>
    <li><svg width="13" height="13" viewBox="0 0 13 13"><circle cx="6.5" cy="6.5" r="6.5" fill="#2a93dc"/><path d="M3.5 6.7l2 2 4-4.2" fill="none" stroke="#fff" stroke-width="1.6"/></svg>But I must explain to you how all this mistaken idea of denouncing</li>
  </ul>
  <p style="top:338px">So if you want us to help yo take your intergrations up a notch, then let's talk.<br><b style="color:var(--ink)">Please call</b> <span class="phone">123 - 456 - 7890</span> or</p>
  <div class="btn btn-outline" style="left:513px;top:413px;width:158px">Bespoke Services</div>
</section>

<section class="where">
  <div class="where-info">
    <div class="eyebrow">Where is Korvane?</div>
    <div class="address">Unit 4, Meridian House, Harlow Business Park<br>Westbrook WB4 2QT</div>
    <div class="where-call">Call Us: <b style="color:var(--white)">123-456-7890</b></div>
    <div class="btn btn-solid" style="left:88px;top:244px;width:158px;background:var(--brand-light)">Send an Email</div>
  </div>
  <div class="map" role="img" aria-label="Street map showing the office location"></div>
</section>

<footer class="site-footer">
  <div class="fcol" style="left:88px"><h3>Company Data</h3><ul><li>Company Information</li><li>Alerts and Notifications</li><li>Contact Information</li><li>Financial Information</li><li>Othe Data Services</li></ul></div>
  <div class="fcol" style="left:353px"><h3>Location Data</h3><ul><li>Postcode Lookup</li><li>Address Lookup</li><li>Base mapping</li><li>Boundaries</li><li>Bespoke Mapping</li></ul></div>
  <div class="fcol" style="left:615px"><h3>Data Services</h3><ul><li>API / Integrations</li><li>Licensing / IPR</li><li>Complex Location Data</li><li>Digital Transformation</li></ul></div>
  <div class="fcol" style="left:880px"><h3>Korvane</h3><ul><li>Pricing</li><li>About Us</li><li>Contact Us</li><li>Free Trial</li><li>Login</li></ul></div>
  <div class="abs footer-mark">KORVANE</div>
  <div class="abs footer-rule"></div>
  <div class="abs copy">© 2019 <b>KORVANE</b>. All Rights Reserved</div>
  <div class="abs legal"><span>Sitemap</span><span>|</span><span>Privacy Policy</span><span>|</span><span>Terms of Use</span><span>|</span><span>Contact Us</span></div>
</footer>

</div>
</body>
</html>
```